I need a business card design for a new company that will be doing consulting work around issues of cultural competency, and diversity and inclusion. I would like the design to be crisp and clear with bold but conservative colors and incorporate shades of blue

Target Market(s)

Small businesses, schools, non-profits

Industry/Entity Type

Consulting

Font styles to use
Serif
Sans Serif

Colors
0c5ba6
6b449b
3276b5
0292cd

Requirements
Must have
• A Morrow Venture (name of company)
• Lemlem Tavish
• CEO
• lemlem@amorrowventure.com
• (215)483-2756

```html
<!DOCTYPE html>
<html lang="en">
<head>
<meta charset="utf-8">
<title>A Morrow Venture – Business Card</title>
<link rel="stylesheet" href="https://fonts.googleapis.com/css2?family=Gelasio:wght@700&family=Roboto:wght@300;400&display=swap">
<style>
  :root {
    --page-bg: #e6e7e9;
    --card-bg: #ffffff;
    --brand-blue: #0292cd;
    --ink: #1f1f1f;
    --ink-soft: #3a3a3a;
    --rule: #2b2b2b;
  }
  * { box-sizing: border-box; margin: 0; padding: 0; }
  html, body {
    width: 1200px;
    height: 1200px;
    overflow: hidden;
    background: var(--page-bg);
  }
  .canvas {
    width: 1200px;
    height: 1200px;
    display: flex;
    align-items: center;
    justify-content: center;
  }
  .business-card {
    position: relative;
    width: 1050px;
    height: 600px;
    background: var(--card-bg);
    box-shadow: 0 6px 24px rgba(0,0,0,0.12);
    overflow: hidden;
  }
  .card-bands {
    position: absolute;
    inset: 0;
    width: 100%;
    height: 100%;
  }
  .card-bands path { fill: var(--brand-blue); }
  .company-name {
    position: absolute;
    top: 52px;
    right: 58px;
    font-family: "Gelasio", Georgia, serif;
    font-weight: 700;
    font-size: 46px;
    color: var(--ink-soft);
    letter-spacing: 0.3px;
  }
  .person-name {
    position: absolute;
    right: 58px;
    top: 282px;
    font-family: "Roboto", Arial, sans-serif;
    font-weight: 300;
    font-size: 44px;
    color: var(--ink);
  }
  .divider {
    position: absolute;
    left: 58px;
    right: 58px;
    top: 342px;
    height: 2px;
    background: var(--rule);
  }
  .person-title {
    position: absolute;
    right: 58px;
    top: 352px;
    font-family: "Roboto", Arial, sans-serif;
    font-weight: 300;
    font-size: 22px;
    color: var(--ink-soft);
    letter-spacing: 1px;
  }
  .contact-list {
    position: absolute;
    left: 58px;
    top: 380px;
    list-style: none;
    font-family: "Roboto", Arial, sans-serif;
    font-weight: 400;
    font-size: 27px;
    color: var(--ink);
  }
  .contact-item {
    display: flex;
    align-items: center;
    gap: 12px;
    margin-bottom: 10px;
  }
  .contact-icon {
    width: 30px;
    height: 30px;
    flex: none;
  }
  .contact-icon circle { fill: var(--brand-blue); }
  .contact-icon .glyph { fill: #fff; }
  .contact-icon text {
    fill: #fff;
    font-family: "Roboto", Arial, sans-serif;
    font-size: 20px;
    font-weight: 400;
  }
</style>
</head>
<body>
<main class="canvas">
  <article class="business-card">
    <svg class="card-bands" viewBox="0 0 1050 600" preserveAspectRatio="none" aria-hidden="true">
      <path class="band-top" d="M0 0 H560 L340 42 C310 48 290 52 260 54 L0 62 Z"/>
      <path class="band-bottom" d="M1050 500 L810 536 C780 541 760 548 735 556 L470 600 H1050 Z"/>
    </svg>

    <h1 class="company-name">A Morrow Venture</h1>

    <p class="person-name">Lemlem Tavish</p>
    <div class="divider"></div>
    <p class="person-title">CEO</p>

    <ul class="contact-list">
      <li class="contact-item">
        <svg class="contact-icon" viewBox="0 0 30 30" aria-hidden="true">
          <circle cx="15" cy="15" r="15"/>
          <path class="glyph" d="M10.5 7.5 C9.5 7.5 8 9 8.3 11 C9 16 14 21.2 19 21.8 C21 22 22.5 20.5 22.5 19.5 L22.3 18.4 L19 16.8 L17.4 18.4 C15 17.4 12.6 15 11.6 12.6 L13.2 11 L11.6 7.7 Z"/>
        </svg>
        <span>(215)483-2756</span>
      </li>
      <li class="contact-item">
        <svg class="contact-icon" viewBox="0 0 30 30" aria-hidden="true">
          <circle cx="15" cy="15" r="15"/>
          <text x="15" y="21.5" text-anchor="middle">@</text>
        </svg>
        <span>lemlem@amorrowventure.com</span>
      </li>
    </ul>
  </article>
</main>
</body>
</html>
```